Tervane Electronic Security Web Site

We need a web site for our new company based in Sydney Australia.
We specialize in consulting supplying and installing electronic security systems. These include CCTV, Access control, Alarms, Intercom and Network cabling.
We pride our selves in giving our customers peace of mind giving back security and freedom to our customers. We pride in customer service quality products and expertise with and we do the job as though it is for our personal friends and family.
We need to be able to edit web site contents and update information.

```html
<!DOCTYPE html>
<html lang="en">
<head>
<meta charset="utf-8">
<title>Tervane Electronic Security</title>
<link rel="stylesheet" href="https://fonts.googleapis.com/css2?family=Open+Sans:ital,wght@0,400;0,600;0,700;1,400&family=Ubuntu:wght@300;400;500;700&display=swap">
<style>
:root{
  --navy:#1a2f5a;
  --navy-text:#1f3566;
  --orange:#f47a24;
  --link:#1e9bd7;
  --grey-text:#9a9a9a;
  --dark-text:#222;
  --footer-bg:#f4f4f4;
  --tile-cctv:#ff9000;
  --tile-access:#fb2153;
  --tile-alarms:#0a78f5;
  --tile-intercom:#3dd65a;
  --tile-cabling:#fb3a26;
}
*{margin:0;padding:0;box-sizing:border-box}
html,body{width:1037px;height:1200px;overflow:hidden;background:#fff}
body{font-family:"Open Sans",Arial,sans-serif;color:var(--dark-text);position:relative}
.page{position:relative;width:1037px;height:1200px;overflow:hidden}
a{text-decoration:none;color:inherit}

/* header */
.brand{position:absolute;left:207px;top:17px;display:flex;align-items:center;gap:7px}
.brand-mark{width:22px;height:22px;background:var(--navy)}
.brand-name{font-family:"Ubuntu",sans-serif;font-weight:700;font-size:14px;color:var(--navy-text)}
.utility{position:absolute;right:207px;top:12px;display:flex;align-items:center;gap:6px;font-size:7.5px;color:var(--grey-text)}
.utility svg{width:7px;height:7px}
.search{width:88px;height:14px;border:1px solid #bbb;border-radius:8px;font-size:6.5px;font-style:italic;padding:2px 7px;color:#aaa;position:relative}
.search svg{position:absolute;right:5px;top:3px}
.nav{position:absolute;right:207px;top:38px;display:flex;gap:12px;font-size:10.5px;color:var(--navy-text)}
.nav span.has-sub::after{content:"";display:inline-block;width:3px;height:3px;border-right:1px solid currentColor;border-bottom:1px solid currentColor;transform:rotate(45deg);margin:0 0 3px 4px}

/* hero */
.hero{position:absolute;left:0;top:58px;width:1037px;height:327px;background:linear-gradient(100deg,#ece6dd 0%,#e6dccf 30%,#c9956a 52%,#e9e1d6 68%,#dfe6ee 85%,#ece9e6 100%)}
.hero-card{position:absolute;left:207px;top:159px;width:296px;height:126px;background:var(--orange);color:#fff;padding:10px 16px}
.hero-card h1{font-family:"Ubuntu",sans-serif;font-weight:300;font-size:26px;line-height:1.2;margin-bottom:9px}
.hero-card p{font-size:9.3px;line-height:15px;margin-left:2px}
.dots{display:flex;gap:4px;margin-top:10px;margin-left:2px}
.dots i{width:5px;height:5px;border:1px solid #fff;border-radius:50%}
.dots i.on{background:#fff}
.to-top{position:absolute;left:943px;top:359px;width:50px;height:27px;background:#fff;display:flex;align-items:center;justify-content:center}

/* services */
.section-title{position:absolute;left:0;width:1037px;text-align:center;font-family:"Ubuntu",sans-serif;font-weight:400}
.help-title{top:406px;font-size:20px;color:#222}
.help-sub{position:absolute;top:443px;left:0;width:1037px;text-align:center;font-size:9px;line-height:15.5px;color:var(--grey-text)}
.services{position:absolute;left:207px;top:496px;display:flex;gap:17px}
.service{width:111px;text-align:center}
.service-tile{width:111px;height:111px;display:flex;align-items:center;justify-content:center}
.service-name{font-family:"Ubuntu",sans-serif;font-size:11.3px;margin-top:8px;color:#222}
.service-more{font-size:9px;color:var(--link);margin-top:6px;display:flex;align-items:center;justify-content:center;gap:3px}
.service-more::before{content:"";width:8px;height:8px;border-radius:50%;background:var(--link)}

/* testimonial */
.testimonial{position:absolute;left:0;top:674px;width:1037px;height:278px;background:var(--navy);color:#fff;text-align:center}
.testimonial h2{font-family:"Ubuntu",sans-serif;font-weight:300;font-size:19.5px;margin-top:22px}
.avatar{width:78px;height:78px;border-radius:50%;margin:20px auto 0;border:3px solid #2c4a80;background:radial-gradient(circle at 50% 40%,#e8c7a8,#c99a6e 60%,#8a6a4a)}
.quote{font-style:italic;font-size:11px;line-height:17.5px;color:#d8deea;margin:14px auto 0;width:640px}
.author{font-family:"Ubuntu",sans-serif;font-size:12px;margin-top:6px}
.testimonial .dots{justify-content:center;margin-top:26px}

/* footer */
.footer-cols{position:absolute;left:207px;top:980px;display:flex}
.footer-col{width:212px}
.footer-col h3{font-family:"Ubuntu",sans-serif;font-weight:400;font-size:14px;color:#222;margin-bottom:8px}
.footer-col a{display:block;font-size:9px;color:var(--link);line-height:19.8px}
.footer-bar{position:absolute;left:0;top:1125px;width:1037px;height:75px;background:var(--footer-bg)}
.legal{position:absolute;left:208px;top:23px;font-size:8px;line-height:14px;color:#888}
.social{position:absolute;left:768px;top:31px;display:flex;gap:2.5px}
.social span{width:13px;height:13px;background:var(--navy)}
</style>
</head>
<body>
<div class="page">

  <header>
    <div class="brand"><span class="brand-mark"></span><span class="brand-name">Tervane Electronic Security</span></div>
    <div class="utility">
      <span>Login | Support |</span>
      <svg viewBox="0 0 10 10"><path d="M2 1l2 2-1 1.5c.8 1.5 1.5 2.2 3 3L7.5 6.5l2 2L8 10C4 9 1 6 0 2z" fill="#aaa"/></svg>
      <span>+61 2 5550 1942</span>
      <div class="search">Search...<svg width="7" height="7" viewBox="0 0 10 10"><circle cx="6" cy="4" r="3" fill="none" stroke="#666" stroke-width="1.2"/><path d="M4 6L1 9" stroke="#666" stroke-width="1.2"/></svg></div>
    </div>
    <nav class="nav">
      <span>Home</span><span>About</span><span class="has-sub">Services</span><span class="has-sub">Solutions</span><span class="has-sub">Products</span><span>Blog</span><span>Contact</span>
    </nav>
  </header>

  <section class="hero" role="img" aria-label="Photo of a smiling family with a child and a fluffy dog in a bright living room">
    <div class="hero-card">
      <h1>Don’t take the chance</h1>
      <p>It to make a type specimen book it has survived not only five centuries, but also the leap into electronic typesetting, remaining essentially unchanged was popularised.</p>
      <div class="dots"><i></i><i class="on"></i><i></i></div>
    </div>
  </section>
  <div class="to-top"><svg width="16" height="10" viewBox="0 0 16 10"><path d="M2 8l6-6 6 6" fill="none" stroke="var(--link)" stroke-width="2"/></svg></div>

  <h2 class="section-title help-title">How can we help you ?</h2>
  <p class="help-sub">Professor at Lakemoor College in Tasmania looked up one of the more obscure<br>Latin words, consectetur discovered the undoubtable source.</p>

  <div class="services">
    <div class="service">
      <div class="service-tile" style="background:var(--tile-cctv)">
        <svg width="76" height="66" viewBox="0 0 76 66" fill="none" stroke="#fff" stroke-width="5" stroke-linejoin="round" stroke-linecap="round"><path d="M18 4L70 30 60 52 10 28z"/><rect x="50" y="34" width="14" height="14" rx="2"/><path d="M12 30c-6 8-4 16 6 20l16 6M30 56h-8"/></svg>
      </div>
      <div class="service-name">CCTV Camera</div>
      <div class="service-more">Learn more</div>
    </div>
    <div class="service">
      <div class="service-tile" style="background:var(--tile-access)">
        <svg width="76" height="66" viewBox="0 0 76 66" fill="none" stroke="#fff" stroke-width="3.5" stroke-linejoin="round"><path d="M25 26a8 8 0 0 1 4-14 11 11 0 0 1 20-2 9 9 0 0 1 3 16z" fill="#fff"/><path d="M38 28v10M30 30l-12 10M46 30l14 10"/><rect x="4" y="40" width="20" height="16"/><rect x="32" y="42" width="10" height="14"/><rect x="50" y="42" width="22" height="14"/><path d="M10 62h8M48 58h26"/></svg>
      </div>
      <div class="service-name">Access Control</div>
      <div class="service-more">Learn more</div>
    </div>
    <div class="service">
      <div class="service-tile" style="background:var(--tile-alarms)">
        <svg width="76" height="70" viewBox="0 0 76 70" fill="none" stroke="#fff" stroke-width="5" stroke-linejoin="round"><path d="M16 10h10v52H16z"/><path d="M30 8l22-4v62l-22-4z" fill="#fff"/><circle cx="60" cy="10" r="6"/></svg>
      </div>
      <div class="service-name">Alarms</div>
      <div class="service-more">Learn more</div>
    </div>
    <div class="service">
      <div class="service-tile" style="background:var(--tile-intercom)">
        <svg width="76" height="76" viewBox="0 0 76 76"><rect x="2" y="6" width="16" height="60" rx="5" fill="#fff"/><rect x="22" y="6" width="52" height="60" rx="3" fill="#fff"/><g fill="var(--tile-intercom)"><rect x="36" y="26" width="8" height="4"/><rect x="48" y="26" width="8" height="4"/><rect x="60" y="26" width="8" height="4"/><rect x="36" y="36" width="8" height="4"/><rect x="48" y="36" width="8" height="4"/><rect x="60" y="36" width="8" height="4"/><rect x="36" y="46" width="8" height="4"/><rect x="48" y="46" width="8" height="4"/><rect x="60" y="46" width="8" height="4"/></g><path d="M10 66a10 8 0 0 0 20 0" fill="none" stroke="#fff" stroke-width="3"/></svg>
      </div>
      <div class="service-name">Intercom</div>
      <div class="service-more">Learn more</div>
    </div>
    <div class="service">
      <div class="service-tile" style="background:var(--tile-cabling)">
        <svg width="70" height="78" viewBox="0 0 70 78" fill="none" stroke="#fff" stroke-width="7" stroke-linecap="round"><path d="M10 58V24a10 10 0 0 1 20 0v34a10 10 0 0 0 20 0V30"/><rect x="42" y="14" width="16" height="18" fill="#fff" stroke="none"/><path d="M47 4v10M53 4v10" stroke-width="3"/></svg>
      </div>
      <div class="service-name">Network Cabling</div>
      <div class="service-more">Learn more</div>
    </div>
  </div>

  <section class="testimonial">
    <h2>What our customer have to say ?</h2>
    <div class="avatar" role="img" aria-label="Portrait photo of the customer"></div>
    <p class="quote">Lettrion sheets containing Lorem Ipsum passages, and more recently with desktop publishing software like Pagewright Studio including versions of Lorem Ipsum etraset sheets containing orem Ipsum passages...</p>
    <p class="author">- Maren Holt, Australia</p>
    <div class="dots"><i></i><i class="on"></i><i></i></div>
  </section>

  <footer>
    <div class="footer-cols">
      <div class="footer-col">
        <h3>About Us</h3>
        <a>Contact Us</a><a>Careers</a><a>Press Room</a><a>Site Map</a><a>Go Homes Realtor Program</a>
      </div>
      <div class="footer-col">
        <h3>Packages</h3>
        <a>Suburbanite Package</a><a>Single Parent Package</a><a>Techie Package</a><a>Elderly/Medical Package</a><a>Basic Package</a>
      </div>
      <div class="footer-col">
        <h3>Philosophy</h3>
        <a>Our Story</a><a>Our Culture</a><a>Our Blog</a><a>Why Tervane</a>
      </div>
    </div>
    <div class="footer-bar">
      <div class="legal">Tervane © 2014<br>Privacy Policy | Terms Of Service | Site Map | Curation Policy</div>
      <div class="social" aria-label="Social links"><span></span><span></span><span></span><span></span></div>
    </div>
  </footer>

</div>
</body>
</html>
```